Marketing Graphics for App

We need a feature graphic to be used in an app store listing for the app Quill Puzzles Plus. Quill Puzzles Plus is a brain training app that allows people to practice various cognitive skills. Our immediate need is for a graphic that can be scaled to run on the Verano Shop Hub free app of the day promotion. This ad will show up on the lock screen on the Tolvo Slate that users will see when the Tolvo Slate is turned on before it is unlocked.

We need a layered PSD file, so that internal elements can be scaled/moved. Please see the guidelines for the graphics ads from Verano.

Concept style guide: https://media-cdn.verano-example.com/docs/ads/VeranoLockCreativeRules.pdf

Technical style guide: https://media-cdn.verano-example.com/docs/ads/VeranoTolvoSlateAdGuide.pdf

I have included some of our existing graphics assets.

See also the app store listing:
http://www.verano-example.com/shop/item/Q77RTWPLMN

Target Market(s)

Mobile phone app users.

Industry/Entity Type

Training

Requirements
Must have
• Text: Quill Puzzles Plus

Text: Exercise Your Brain
Possibly add: Brain Training Games

```html
<!DOCTYPE html>
<html lang="en">
<head>
<meta charset="utf-8">
<title>Quill Puzzles Plus – Feature Graphic</title>
<link rel="stylesheet" href="https://fonts.googleapis.com/css2?family=Quicksand:wght@300;400;700&display=swap">
<style>
  :root {
    --sky: #8ecbe4;
    --sky-light: #b3dced;
    --sky-deep: #7fc2de;
    --brand-blue: #8dcae3;
    --white: #ffffff;
  }
  html, body {
    margin: 0;
    padding: 0;
    width: 1200px;
    height: 703px;
    overflow: hidden;
    background: var(--sky);
  }
  .feature-graphic {
    position: relative;
    width: 1200px;
    height: 703px;
    overflow: hidden;
    font-family: "Quicksand", sans-serif;
  }
  .ring-backdrop {
    position: absolute;
    inset: 0;
    background: radial-gradient(circle at 50% 48%, var(--sky-light) 0%, var(--sky) 35%, var(--sky-deep) 75%, var(--sky-light) 100%);
  }
  .brand-mark {
    position: absolute;
    left: 472px;
    top: 46px;
    width: 256px;
    height: 256px;
    border-radius: 50%;
    background: var(--white);
  }
  .title-plate {
    position: absolute;
    left: 319px;
    top: 357px;
    width: 595px;
    height: 94px;
    background: var(--white);
    border-radius: 22px 6px 22px 6px;
    display: flex;
    align-items: center;
    justify-content: center;
  }
  .app-name {
    margin: 0;
    font-weight: 700;
    font-size: 50px;
    letter-spacing: 0.5px;
    color: var(--brand-blue);
    line-height: 1;
  }
  .tagline {
    position: absolute;
    left: 0;
    right: 0;
    top: 482px;
    margin: 0;
    text-align: center;
    color: var(--white);
    font-weight: 300;
    line-height: 1;
  }
  .tagline-main {
    display: block;
    font-size: 54px;
    letter-spacing: 1px;
  }
  .tagline-joiner {
    display: block;
    font-size: 31px;
    margin-top: 2px;
  }
  .tagline-sub {
    display: block;
    font-size: 50px;
    letter-spacing: 1px;
    margin-top: 6px;
  }
</style>
</head>
<body>
  <main class="feature-graphic">
    <div class="ring-backdrop" role="img" aria-label="Soft light blue background of concentric rings radiating from the centre"></div>
    <div class="brand-mark" aria-hidden="true"></div>
    <div class="title-plate">
      <h1 class="app-name">Quill Puzzles Plus</h1>
    </div>
    <p class="tagline">
      <span class="tagline-main">Exercise Your Brain</span>
      <span class="tagline-joiner">with</span>
      <span class="tagline-sub">Brain Training Games</span>
    </p>
  </main>
</body>
</html>
```